Dune Haulers Catalogue Template Design

We need a new fresh brand design for our business in the form of a catalogue layout. Dune Haulers is a Fuel transportation company and we have specialised tank trucks to deliver gasoline. The catalogue should provide a feeling of motion. Colours to be used: RED, GREY, BLACKWe like the use of parallelograms and geometric motion patterns. The Catalogue should provide a feeling of motion. We have included some notes on design concepts that we like. Please look at this brief as this will guide you in your design process.We will use this catalogue concept to design our company corporate identity. Final designs should communicate sophistication and success

```html
<!DOCTYPE html>
<html lang="en">
<head>
<meta charset="utf-8">
<title>Dune Haulers Catalogue Covers</title>
<link rel="stylesheet" href="https://fonts.googleapis.com/css2?family=Montserrat:wght@300;400;600;800;900&display=swap">
<style>
  :root {
    --red: #d21f2b;
    --red-dark: #8e1218;
    --black: #161616;
    --charcoal: #2b2b2b;
    --grey: #8a8a8a;
    --grey-light: #d9d9d9;
    --paper: #f3f3f3;
    --white: #ffffff;
    --stage: #e9e9e9;
  }
  * { box-sizing: border-box; margin: 0; padding: 0; }
  html, body { width: 900px; height: 1200px; overflow: hidden; }
  body {
    background: var(--stage);
    font-family: "Montserrat", Arial, sans-serif;
    position: relative;
  }
  .cover {
    position: absolute;
    left: 40px;
    width: 820px;
    height: 560px;
    overflow: hidden;
    background: var(--paper);
    box-shadow: 0 4px 14px rgba(0,0,0,0.25);
  }
  .cover--front { top: 30px; }
  .cover--back { top: 620px; }
  .cover-art { position: absolute; inset: 0; width: 100%; height: 100%; }

  .brand {
    position: absolute;
    display: flex;
    align-items: center;
    gap: 8px;
    color: var(--red);
    font-weight: 800;
    font-size: 20px;
  }
  .brand-dot {
    width: 22px; height: 22px;
    border-radius: 50%;
    background: var(--red);
  }
  .cover--front .brand { top: 26px; right: 26px; }
  .cover--back .brand { bottom: 24px; right: 26px; }

  .cover-title {
    position: absolute;
    left: 500px;
    top: 160px;
    color: var(--black);
    font-weight: 900;
    font-size: 66px;
    line-height: 0.98;
    letter-spacing: 1px;
  }
  .cover-tagline {
    position: absolute;
    left: 470px;
    top: 332px;
    color: var(--white);
    font-size: 34px;
    line-height: 1.05;
    font-weight: 300;
    letter-spacing: 1px;
  }
  .cover-tagline strong { font-weight: 800; display: block; }
  .cover-welcome {
    position: absolute;
    right: 24px;
    bottom: 18px;
    font-size: 11px;
    color: var(--charcoal);
  }

  .contact-list {
    position: absolute;
    left: 70px;
    top: 262px;
    list-style: none;
    color: var(--white);
    font-size: 17px;
    line-height: 1.35;
  }
  .contact-item { display: flex; align-items: flex-start; gap: 12px; margin-bottom: 14px; }
  .contact-icon { width: 16px; height: 16px; flex: none; margin-top: 3px; }
  .cover-credit {
    position: absolute;
    left: 24px;
    bottom: 18px;
    font-size: 10px;
    color: var(--white);
    opacity: 0.8;
  }
</style>
</head>
<body>

<section class="cover cover--front">
  <svg class="cover-art" viewBox="0 0 820 560" aria-hidden="false">
    <defs>
      <linearGradient id="fleetPhoto" x1="0" y1="0" x2="0" y2="1">
        <stop offset="0" stop-color="#cdd7e0"/>
        <stop offset="0.45" stop-color="#aab3bb"/>
        <stop offset="0.62" stop-color="#e8e8e8"/>
        <stop offset="0.74" stop-color="#d21f2b"/>
        <stop offset="1" stop-color="#8e1218"/>
      </linearGradient>
    </defs>
    <polygon points="300,0 420,0 700,560 580,560" fill="#e6e6e6"/>
    <polygon points="470,0 560,0 820,520 820,560 760,560" fill="#ebebeb"/>
    <polygon points="0,0 270,0 530,560 0,560" fill="url(#fleetPhoto)" role="img" aria-label="Photo of a tanker truck fleet parked before a city skyline"/>
    <polygon points="270,0 305,0 565,560 530,560" fill="var(--black)"/>
    <polygon points="320,0 334,0 594,560 580,560" fill="var(--charcoal)"/>
    <polygon points="0,40 60,0 80,0 0,54" fill="var(--black)"/>
    <polygon points="470,305 820,305 820,410 420,410" fill="var(--red)"/>
    <polygon points="420,410 820,410 820,420 416,420" fill="var(--black)"/>
  </svg>

  <div class="brand"><span class="brand-dot"></span>Dune Haulers</div>
  <h1 class="cover-title">COVER<br>DESIGN</h1>
  <p class="cover-tagline">DRIVEN BY <strong>PASSION</strong></p>
  <p class="cover-welcome">Welcome to Dune Haulers</p>
</section>

<section class="cover cover--back">
  <svg class="cover-art" viewBox="0 0 820 560">
    <defs>
      <linearGradient id="roadPhoto" x1="0" y1="0" x2="1" y2="1">
        <stop offset="0" stop-color="#d8d8d8"/>
        <stop offset="0.5" stop-color="#9a9a9a"/>
        <stop offset="1" stop-color="#4a4a4a"/>
      </linearGradient>
    </defs>
    <polygon points="0,0 560,0 430,560 0,560" fill="url(#roadPhoto)" role="img" aria-label="Black and white photo of a tanker truck on the road with a city skyline behind"/>
    <polygon points="600,0 700,0 560,560 460,560" fill="var(--grey)"/>
    <polygon points="720,0 820,0 820,120 690,560 600,560" fill="#bdbdbd"/>
    <polygon points="560,0 600,0 460,560 430,560" fill="var(--black)"/>
    <polygon points="0,230 545,230 505,400 0,400" fill="var(--charcoal)" opacity="0.92"/>
    <polygon points="0,400 505,400 502,410 0,410" fill="var(--red)"/>
  </svg>

  <ul class="contact-list">
    <li class="contact-item">
      <svg class="contact-icon" viewBox="0 0 16 16"><path d="M8 1a5 5 0 0 0-5 5c0 4 5 9 5 9s5-5 5-9a5 5 0 0 0-5-5zm0 7a2 2 0 1 1 0-4 2 2 0 0 1 0 4z" fill="var(--red)"/></svg>
      <span>14 Marlow Road, Kestrel Park<br>P O Box 2207, Eastvale, 2210</span>
    </li>
    <li class="contact-item">
      <svg class="contact-icon" viewBox="0 0 16 16"><path d="M4 1l3 3-2 2c1 2 3 4 5 5l2-2 3 3-2 3C7 15 1 9 1 3z" fill="var(--red)"/></svg>
      <span>(010) 555 0192</span>
    </li>
    <li class="contact-item">
      <svg class="contact-icon" viewBox="0 0 16 16"><circle cx="8" cy="8" r="6.5" fill="none" stroke="var(--red)" stroke-width="1.6"/><path d="M1.5 8h13M8 1.5c-3 3.5-3 9.5 0 13M8 1.5c3 3.5 3 9.5 0 13" fill="none" stroke="var(--red)" stroke-width="1.2"/></svg>
      <span>www.dunehaulers.example</span>
    </li>
  </ul>

  <p class="cover-credit">© Dune Haulers 2024</p>
  <div class="brand"><span class="brand-dot"></span>Dune Haulers</div>
</section>

</body>
</html>
```